Hong Kong residential leasing and sales company needs a website design

Hong Kong has many competitive real estate agents. The majority of us have the same listings so, besides the team and experience, a website is what makes us stand out. A first impression. We need our website to be user friendly, informative and to have a wow factor. Most sites are generic so whilst we are close to accepting that maybe that's the only formula which works....we would like to see if we're missing something! Our clients are a mix of International users of all ages but probably ultimately 35+.. We have a logo (attached) which we would like to keep - designed by brushforum. Flexible with colours except red.
examples of our competitors are:
http://www.marlowvesthomes.example
http://www.tuvix.example/home
http://www.premierdwellingsgr.example
http://www.nestora-estates.example
http://www.fieldmark-ardley.example
We were thinking of having the following in a menu bar with drop downs for most...some more than others. Home / For Sale / For Rent / Property 101 / About us / Contact Us ..
Look forward to seeing your ideas. Thanks in advance.

```html
<!DOCTYPE html>
<html lang="en">
<head>
<meta charset="utf-8">
<title>Kestrel Homes</title>
<link href="https://fonts.googleapis.com/css2?family=Open+Sans:wght@400;600;700&display=swap" rel="stylesheet">
<style>
:root{
  --purple:#6a2f8e;
  --purple-bright:#9b3fc8;
  --purple-dark:#4b2068;
  --ink:#333;
  --muted:#666;
  --faint:#aaa;
  --line:#d8d8d8;
  --panel:#f5f5f5;
  --dark-btn:#3a3a3a;
  --tab-grey:#6b6b6b;
}
*{box-sizing:border-box;margin:0;padding:0}
html,body{width:866px;height:1200px;overflow:hidden;background:#fff}
body{position:relative;font-family:"Open Sans",Arial,sans-serif;color:var(--ink)}
.abs{position:absolute}
.top-rule{left:0;top:0;width:866px;height:3px;background:var(--purple-dark)}
.brand-column{left:53px;top:3px;width:185px;height:400px;background:linear-gradient(#efefef,#fff 55%)}
.brand{left:53px;top:40px;width:185px;text-align:center}
.brand-mark{display:inline-block;width:22px;height:22px;background:var(--purple);margin-bottom:10px}
.brand-name{font-size:20px;font-weight:700;letter-spacing:3px;color:#1a1a1a;text-transform:uppercase;line-height:1.2}
.brand-rule{left:62px;top:142px;width:168px;height:2px;background:#ccc}
.enquiries{right:262px;top:38px;font-size:12px;color:var(--muted);letter-spacing:.3px;display:flex;align-items:center;gap:6px}
.enquiries b{font-weight:400;color:var(--purple-dark)}
.site-search{left:702px;top:34px;width:111px;height:25px;border:1px solid #ccc;border-radius:3px;background:#fafafa}
.site-search .btn{position:absolute;right:0;top:0;width:22px;height:23px;border-left:1px solid #ccc;display:flex;align-items:center;justify-content:center}
.header-rule{left:248px;top:79px;width:565px;height:1px;background:var(--line)}
.main-nav{left:355px;top:90px;display:flex;font-size:10px;text-transform:uppercase;color:#222;letter-spacing:.2px}
.main-nav span{height:29px;line-height:29px;padding:0 14.5px}
.main-nav .active{background:var(--purple);color:#fff;font-weight:600;padding:0 15px}
.finder{left:62px;top:155px;width:168px;height:239px}
.finder-tabs{display:flex;font-size:9px;text-transform:uppercase}
.finder-tabs span{height:25px;line-height:25px;padding:0 19px}
.finder-tabs .on{border:1px solid var(--line);border-bottom:none;background:#fff;color:var(--purple);position:relative;top:1px}
.finder-body{border:1px solid var(--line);height:214px;padding:10px 12px;font-size:9px;color:#333}
.finder-body label{display:block;margin-bottom:3px}
.select{height:19px;border:1px solid #ccc;border-radius:2px;background:linear-gradient(#fff,#f0f0f0);position:relative;margin-bottom:9px}
.select::after{content:"";position:absolute;right:6px;top:8px;border:3px solid transparent;border-top-color:#888}
.price-row{display:flex;align-items:flex-start;gap:6px}
.price-row .select{width:57px}
.price-row span{line-height:19px;padding:0 3px}
.search-now{margin-top:12px;width:114px;height:25px;background:var(--dark-btn);color:#fff;font-size:9px;display:flex;align-items:center;justify-content:center;gap:6px;border-radius:2px}
.hero{left:248px;top:129px;width:565px;height:277px;border:1px solid var(--line);padding:2px}
.hero-photo{width:100%;height:100%;background:linear-gradient(120deg,#7a2a2a 0%,#e6e1da 35%,#8a2f2a 55%,#b27a4a 85%,#c69060 100%)}
.hero-caption{left:519px;top:226px;width:293px;height:83px;background:rgba(35,25,30,.85);padding:8px 18px;color:#fff}
.hero-caption h1{font-weight:400;font-size:24px;line-height:1.2}
.hero-caption p{font-size:8.5px;margin-top:6px}
.hero-caption .price{font-size:14px;color:var(--purple-bright);margin-top:5px;font-weight:600}
.dots{left:507px;top:385px;display:flex;gap:5px}
.dots i{width:8px;height:8px;border-radius:50%;background:#fff}
.dots i:first-child{background:#111}
.listing-tabs{left:53px;top:428px;display:flex;align-items:center;font-size:9.5px;color:var(--faint);text-transform:uppercase}
.listing-tabs span{margin-right:29px}
.listing-tabs .on{background:var(--purple);color:#fff;height:29px;line-height:29px;padding:0 16px;position:relative;font-size:10px;letter-spacing:.3px;margin-right:22px}
.listing-tabs .on::after{content:"";position:absolute;left:66px;bottom:-6px;border:6px solid transparent;border-bottom:none;border-top-color:var(--purple)}
.card{width:175px;height:200px;border:1px solid var(--line);padding:7px 8px}
.card-photo{height:103px}
.card h3{font-size:9.5px;font-weight:600;margin-top:11px;letter-spacing:.2px}
.card p{font-size:8.5px;color:var(--muted);line-height:15.5px;margin-top:1px}
.card .price{font-size:12px;color:var(--purple-bright);margin-top:5px}
.section-rule{left:53px;top:909px;width:760px;height:2px;background:var(--line)}
.about{left:53px;top:922px;width:230px}
.about h2{font-size:12.5px;color:var(--purple-dark);font-weight:400}
.about p{font-size:8px;color:var(--muted);line-height:13.3px;margin-top:9px}
.read-more{display:inline-block;margin-top:10px;background:var(--dark-btn);color:#fff;font-size:8px;padding:5px 9px;border-radius:1px}
.advice-tabs{left:313px;top:926px;display:flex;gap:5px;font-size:11px;text-transform:uppercase}
.advice-tabs span{height:25px;line-height:25px;width:136px;text-align:center;background:var(--tab-grey);color:#eee}
.advice-tabs .on{background:#fff;color:var(--purple);border:1px solid var(--line);border-bottom:none;height:26px;width:134px}
.advice-panel{left:313px;top:951px;width:500px;height:137px;border:1px solid var(--line)}
.experts{left:328px;top:968px;display:flex;gap:14px}
.expert{width:108px;text-align:center}
.expert-photo{height:89px;border:1px solid #ccc;padding:2px}
.expert-photo div{width:100%;height:100%}
.expert span{display:block;font-size:8.5px;color:var(--purple);margin-top:8px}
.footer{left:0;top:1106px;width:866px;height:94px;background:#efefef}
.footer-brand{left:53px;top:1119px;display:flex;align-items:center;gap:5px;font-size:11px;font-weight:700;letter-spacing:1.5px;text-transform:uppercase}
.footer-brand i{width:10px;height:10px;background:var(--purple)}
.subscribe{right:53px;top:1125px;display:flex;align-items:center;gap:7px;font-size:10px;color:var(--purple-dark);letter-spacing:.3px}
.subscribe .field{width:143px;height:19px;border:1px solid #ccc;background:#fff;font-size:7px;font-style:italic;color:#888;line-height:17px;padding-left:9px;position:relative}
.subscribe .go{position:absolute;right:0;top:-1px;width:19px;height:19px;background:var(--purple-dark);display:flex;align-items:center;justify-content:center}
.legal{left:53px;top:1173px;font-size:8px;color:var(--muted)}
.footer-nav{right:53px;top:1173px;font-size:8px;color:var(--muted)}
</style>
</head>
<body>
<div class="abs top-rule"></div>
<div class="abs brand-column"></div>
<div class="abs brand">
  <div class="brand-mark"></div>
  <div class="brand-name">Kestrel<br>Homes</div>
</div>
<div class="abs brand-rule"></div>

<div class="abs enquiries">
  <svg width="9" height="11" viewBox="0 0 9 11"><path d="M2 0h2l1 3-1.5 1c.5 1.5 1.3 2.5 2.5 3.3L7 6l2 1.5V10c-5 0-9-4.5-9-10z" fill="#c0392b"/></svg>
  ENQUIRIES: <b>+852 3140 7720</b>
</div>
<div class="abs site-search"><div class="btn"><svg width="11" height="11" viewBox="0 0 11 11"><circle cx="4.5" cy="4.5" r="3.2" fill="none" stroke="#6a2f8e" stroke-width="1.5"/><path d="M7 7l3.3 3.3" stroke="#6a2f8e" stroke-width="1.8"/></svg></div></div>
<div class="abs header-rule"></div>
<nav class="abs main-nav">
  <span class="active">Home</span><span>For Sale</span><span>For Rent</span><span>Property 101</span><span>About Us</span><span>Contact Us</span>
</nav>

<div class="abs finder">
  <div class="finder-tabs"><span class="on">Rent</span><span>Buy</span></div>
  <div class="finder-body">
    <label>Location:</label><div class="select"></div>
    <label>Size:</label><div class="select"></div>
    <label>Price:</label>
    <div class="price-row"><div class="select"></div><span>To</span><div class="select"></div></div>
    <label>Bedroom</label><div class="select" style="width:57px"></div>
    <div class="search-now"><svg width="10" height="10" viewBox="0 0 11 11"><circle cx="6.5" cy="4.5" r="3.2" fill="none" stroke="#fff" stroke-width="1.5"/><path d="M4 7L.7 10.3" stroke="#fff" stroke-width="1.8"/></svg>SEARCH NOW</div>
  </div>
</div>

<div class="abs hero"><div class="hero-photo" role="img" aria-label="Empty living room with red walls, large arched window, chandelier and wooden floor"></div></div>
<div class="abs hero-caption">
  <h1>Splendour Villa</h1>
  <p>SA1,027 sq ft &nbsp;|&nbsp; GA1,332 sq ft &nbsp;|&nbsp; 2 bedrooms, 2 bathrooms</p>
  <div class="price">HK$68,000</div>
</div>
<div class="abs dots"><i></i><i></i><i></i><i></i></div>

<div class="abs listing-tabs">
  <span class="on">Featured Properties</span><span>New Additions</span><span>For Rent</span><span>For Sale</span><span>Serviced Apartments</span>
</div>

<div class="abs card" style="left:53px;top:475px"><div class="card-photo" role="img" aria-label="Modern villa terrace at dusk with dining area and pool" style="background:linear-gradient(100deg,#c89060,#5a3a2a 55%,#1a2a6a)"></div><h3>DRAGON LAKE VILLA</h3><p>SA2,350 sq ft / GA2,480 sq ft<br>4 bedrooms, 2 bathrooms</p><div class="price">HK$129,000</div></div>
<div class="abs card" style="left:248px;top:475px"><div class="card-photo" role="img" aria-label="White modern house with swimming pool under blue sky" style="background:linear-gradient(#3a6ab0,#e8eef2 55%,#2aa0c8)"></div><h3>DRAGON LAKE VILLA</h3><p>SA2,350 sq ft / GA2,480 sq ft<br>4 bedrooms, 2 bathrooms</p><div class="price">HK$129,000</div></div>
<div class="abs card" style="left:443px;top:475px"><div class="card-photo" role="img" aria-label="Mediterranean style house with palm trees and garage" style="background:linear-gradient(#5a8ac8,#c8b090 55%,#5a7a3a)"></div><h3>DRAGON LAKE VILLA</h3><p>SA2,350 sq ft / GA2,480 sq ft<br>4 bedrooms, 2 bathrooms</p><div class="price">HK$129,000</div></div>
<div class="abs card" style="left:638px;top:475px"><div class="card-photo" role="img" aria-label="Double height living room with turquoise walls and white sofa" style="background:linear-gradient(100deg,#4ab0c0,#d8dcdc 50%,#5a4a40)"></div><h3>DRAGON LAKE VILLA</h3><p>SA2,350 sq ft / GA2,480 sq ft<br>4 bedrooms, 2 bathrooms</p><div class="price">HK$129,000</div></div>

<div class="abs card" style="left:53px;top:689px"><div class="card-photo" role="img" aria-label="Bright hallway with wooden staircase" style="background:linear-gradient(100deg,#e8e2d8,#c89060 70%,#f0ece6)"></div><h3>DRAGON LAKE VILLA</h3><p>SA2,350 sq ft / GA2,480 sq ft<br>4 bedrooms, 2 bathrooms</p><div class="price">HK$129,000</div></div>
<div class="abs card" style="left:248px;top:689px"><div class="card-photo" role="img" aria-label="Row of modern townhouses with red and white facades" style="background:linear-gradient(#2a4a9a,#b03a3a 50%,#6a6a6a)"></div><h3>DRAGON LAKE VILLA</h3><p>SA2,350 sq ft / GA2,480 sq ft<br>4 bedrooms, 2 bathrooms</p><div class="price">HK$129,000</div></div>
<div class="abs card" style="left:443px;top:689px"><div class="card-photo" role="img" aria-label="Warm lit bedroom with white bed" style="background:linear-gradient(#d88a40,#f0d0a0 50%,#e8e0d8)"></div><h3>DRAGON LAKE VILLA</h3><p>SA2,350 sq ft / GA2,480 sq ft<br>4 bedrooms, 2 bathrooms</p><div class="price">HK$129,000</div></div>
<div class="abs card" style="left:638px;top:689px"><div class="card-photo" role="img" aria-label="Living room with sofas and large windows" style="background:linear-gradient(100deg,#8a6a5a,#d8d0c8 50%,#6a8a5a)"></div><h3>DRAGON LAKE VILLA</h3><p>SA2,350 sq ft / GA2,480 sq ft<br>4 bedrooms, 2 bathrooms</p><div class="price">HK$129,000</div></div>

<div class="abs section-rule"></div>

<section class="abs about">
  <h2>About Our Company</h2>
  <p>Lorem ipsum dolor sit amet, consect- etuer adipiscing elit, sed diam nonummy nibh euismod tincidunt ut laoreet dolore magna aliquam erat volutpat. Ut wisi enim ad minim veniam, quis nostrud exerci tation ullam..</p>
  <p style="margin-top:6px">Consectetuer adipiscing elit, sed diam nonummy nibh euismod tincidunt ut laoreet dolore magna aliquam erat volut- pat. Ut wisi enim ad minim veniam, quis nostrud exerci tation ullam.</p>
  <span class="read-more">READ MORE</span>
</section>

<div class="abs advice-panel"></div>
<div class="abs advice-tabs"><span class="on">Expert's Advice</span><span>What's New</span><span>Update Blog's</span></div>
<div class="abs experts">
  <div class="expert"><div class="expert-photo"><div role="img" aria-label="Portrait of property adviser" style="background:linear-gradient(#b8c0b0,#3a3a40)"></div></div><span>Darren KL Wong</span></div>
  <div class="expert"><div class="expert-photo"><div role="img" aria-label="Portrait of property adviser" style="background:linear-gradient(#f4f4f4,#2a2a2e)"></div></div><span>Darren KL Wong</span></div>
  <div class="expert"><div class="expert-photo"><div role="img" aria-label="Portrait of property adviser" style="background:linear-gradient(#eeeeee,#222226)"></div></div><span>Darren KL Wong</span></div>
  <div class="expert"><div class="expert-photo"><div role="img" aria-label="Portrait of property adviser" style="background:linear-gradient(#f0f0f0,#3a3030)"></div></div><span>Vivian Lau</span></div>
</div>

<footer>
  <div class="abs footer"></div>
  <div class="abs footer-brand"><i></i>Kestrel Homes</div>
  <div class="abs subscribe">SUBSCRIBE NEWSLETTER:
    <div class="field">Enter Email Address<div class="go"><svg width="8" height="9" viewBox="0 0 8 9"><path d="M2 1l4 3.5L2 8" fill="none" stroke="#fff" stroke-width="1.8"/></svg></div></div>
  </div>
  <div class="abs legal">Copyright © 2014. All Right Reserved &nbsp;|&nbsp; Privacy Plicy &nbsp;|&nbsp; Term of Services</div>
  <div class="abs footer-nav">Home &nbsp;/&nbsp; For Sale &nbsp;/&nbsp; For Rent &nbsp;/&nbsp; Property 101 &nbsp;/&nbsp; About us &nbsp;/&nbsp; Contact Us</div>
</footer>
</body>
</html>
```